Tidewell HVAC WordPress website design

Design a new modern, clean, website for HVAC mechanical business that uses company logo/colors for branding and recognition. Files attached are just for band and color information. Here is a website design that appeals to me https://www.quillerbyhomes.example/

A clear description of who we are and what we do

An easily-navigated site map

An easily-navigated site map for mobile devices

Easy-to-find contact information

Obvious call to action for service, installs or to schedule estimates

about us page

Provide a way for potential customers to contact us via text or email

provide a way that allows a customer to upload a picture to request a service call or quote.
Updates

I'm looking for the design to be completed in WordPress

Industry/Entity Type

HVAC Mechanical & Building Automation / Controls contractor

Coding

Coded - Design and coding required

Number of Pages Required

5+ page

Colors
0054AA
0677BA
7BADD7
CADEEF
E8F1F8

Requirements
Must have
• Design a new modern, clean, website for HVAC mechanical business that uses company logo/colors for branding and recognition. Files attached are just for band and color information. Here is a website design that appeals to me https://www.quillerbyhomes.example/ A clear description of who we are and what we do An easily-navigated site map An easily-navigated site map for mobile devices Easy-to-find contact information Obvious call to action for service, installs or to schedule estimates about us page Provide a way for potential customers to contact us via text or email provide a way that allows a customer to upload a picture to request a service call or quote.
Nice to have

```html
<!DOCTYPE html>
<html lang="en">
<head>
<meta charset="utf-8">
<title>Tidewell HVAC – Heating &amp; Air Conditioning</title>
<link href="https://fonts.googleapis.com/css2?family=Poppins:wght@400;500;600&display=swap" rel="stylesheet">
<style>
:root{
  --navy:#1d1b5e;
  --navy-deep:#15134a;
  --blue:#1a73e8;
  --blue-soft:#7badd7;
  --ink:#1f2340;
  --muted:#5b6072;
  --line:#cadeef;
  --tint:#f4f6f9;
  --canvas:#eceff3;
  --white:#ffffff;
}
*{box-sizing:border-box;margin:0;padding:0}
html,body{width:1200px;height:4121px;overflow:hidden;background:var(--canvas);font-family:"Poppins",sans-serif;color:var(--ink)}
.page{position:absolute;left:40px;top:0;width:1120px;height:4121px;background:var(--white);overflow:hidden}
.abs{position:absolute}
.btn{position:absolute;display:flex;align-items:center;justify-content:center;border-radius:20px;font-size:11px;font-weight:500;white-space:nowrap}
.btn-outline{border:1.5px solid var(--blue);color:var(--blue);background:var(--white)}
.btn-solid{background:var(--blue);color:var(--white)}
.btn-navy{background:var(--navy);color:var(--white)}
.btn-ghost{border:1.5px solid var(--blue);color:var(--white)}

/* header */
.brand{position:absolute;display:flex;align-items:center;gap:10px;font-weight:600;color:var(--navy)}
.brand-dot{border-radius:50%;background:var(--blue)}
.nav{position:absolute;left:388px;top:96px;width:640px;display:flex;justify-content:space-between;font-size:11px;color:var(--ink)}
.nav .active{color:var(--blue);border-bottom:2px solid var(--blue);padding-bottom:3px}

/* hero */
.hero-photo{position:absolute;left:0;top:130px;width:1120px;height:540px;background:linear-gradient(100deg,#eef2f7 0%,#d8e0ea 45%,#aab8c9 75%,#c9d3df 100%)}
.eyebrow{position:absolute;left:98px;top:290px;font-size:13px;color:var(--blue);font-weight:500}
.hero-title{position:absolute;left:98px;top:318px;font-size:27px;line-height:35px;font-weight:500;color:var(--navy)}
.badge{position:absolute;width:132px;height:132px;border-radius:50%;background:var(--navy);border:5px solid var(--white);box-shadow:0 0 0 3px var(--blue);color:var(--white);text-align:center;display:flex;flex-direction:column;align-items:center;justify-content:center}
.badge b{font-size:40px;font-weight:500;line-height:40px}
.badge span{font-size:10px;font-weight:500;line-height:12px}

/* form */
.form-panel{position:absolute;left:656px;top:494px;width:280px;height:496px;background:var(--navy);color:var(--white);text-align:center;padding:30px 23px 0}
.form-panel h3{font-size:15px;font-weight:400}
.form-panel h4{font-size:15px;font-weight:600;margin-top:6px;margin-bottom:20px}
.field{height:32px;background:var(--white);border-radius:2px;margin-bottom:15px;font-size:9px;color:var(--muted);text-align:left;padding:10px 10px;display:flex;justify-content:space-between}
.field.tall{height:40px}
.submit{height:32px;border-radius:16px;background:var(--blue);font-size:11px;font-weight:500;display:flex;align-items:center;justify-content:center;margin-top:20px}
.call-label{font-size:9px;font-weight:600;margin-top:30px}
.call-num{font-size:20px;color:var(--blue);font-weight:500}

/* about */
.section-title{position:absolute;font-size:23px;line-height:30px;font-weight:500;color:var(--navy)}
.body-copy{position:absolute;font-size:9px;line-height:15px;color:var(--muted)}
.center{text-align:center}
.rule{position:absolute;height:2px;background:var(--blue)}

/* trust */
.trust-item{position:absolute;width:160px;text-align:center;font-size:9.5px;line-height:13px;color:var(--navy);font-weight:500}
.trust-item svg{display:block;margin:0 auto 18px}

/* services band */
.services-bg{position:absolute;left:0;top:1350px;width:1120px;height:836px;background:linear-gradient(180deg,#e4e7ec 0%,#f2f3f5 50%,#e8ebef 100%)}
.cat{position:absolute;width:180px;height:180px;border-radius:50%;border:5px solid var(--blue);display:flex;align-items:center;justify-content:center;color:var(--white);font-size:12px;font-weight:500;text-align:center;line-height:15px}
.card{position:absolute;width:170px;height:138px;background:var(--white);box-shadow:0 2px 10px rgba(30,40,80,.08);display:flex;flex-direction:column;align-items:center;justify-content:center;gap:12px;font-size:10.5px;font-weight:500;color:var(--navy)}
.card.on{background:linear-gradient(180deg,var(--blue) 0%,var(--navy) 100%);color:var(--white)}

/* community */
.community-photo{position:absolute;left:0;top:2186px;width:620px;height:480px;background:linear-gradient(160deg,#e9c2a4 0%,#8f9aa8 45%,#4f5f74 100%)}
.community-panel{position:absolute;left:0;top:2186px;width:1120px;height:480px;background:var(--navy);clip-path:polygon(506px 0,1120px 0,1120px 480px,552px 480px)}
.light{color:#d9defa}

/* testimonials */
.reviews-bg{position:absolute;left:0;top:2660px;width:1120px;height:454px;background:var(--tint)}
.review{position:absolute;top:2780px;width:236px;height:140px;background:var(--white);padding:18px 16px;box-shadow:0 2px 8px rgba(30,40,80,.06)}
.stars{color:var(--blue);font-size:10px;letter-spacing:2px}
.review p{font-size:8.5px;line-height:14px;color:var(--muted);margin-top:6px}
.reviewer{position:absolute;top:2948px;display:flex;align-items:center;gap:14px;font-size:10.5px;color:var(--navy)}
.quote{width:30px;height:30px;border-radius:50%;background:var(--navy);color:var(--white);font-size:18px;font-weight:600;display:flex;align-items:center;justify-content:center;padding-top:8px}
.arrow{position:absolute;top:2840px;font-size:18px;color:var(--navy)}

/* partners */
.seal{position:absolute;background:#d5dbe4}

/* careers */
.careers{position:absolute;left:0;top:3340px;width:1120px;height:440px;background:linear-gradient(180deg,var(--navy) 0%,#28266e 60%,var(--navy-deep) 100%)}
.careers-title{position:absolute;top:3496px;width:1120px;text-align:center;color:var(--white);font-size:21px;line-height:29px;font-weight:500}
.careers-copy{position:absolute;top:3606px;width:1120px;text-align:center;color:#dfe3f7;font-size:14px;line-height:23px}

/* footer */
.foot-h{position:absolute;font-size:11px;font-weight:600;color:var(--navy)}
.foot-list{position:absolute;font-size:9.5px;line-height:17px;color:var(--ink);list-style:none}
.contact-row{display:flex;gap:10px;align-items:flex-start}
.social{position:absolute;top:3970px;width:22px;height:22px;border-radius:50%;border:1.5px solid var(--blue)}
.legal{position:absolute;top:4076px;font-size:9px;color:var(--ink)}
</style>
</head>
<body>
<div class="page">

  <!-- Header -->
  <div class="brand" style="left:98px;top:62px;font-size:20px"><span class="brand-dot" style="width:30px;height:30px"></span>Tidewell HVAC</div>
  <div class="btn btn-outline" style="left:702px;top:56px;width:156px;height:30px;font-size:9.5px">Schedule an Appointment</div>
  <div class="btn btn-solid" style="left:884px;top:56px;width:140px;height:30px;font-size:9.5px">
    <svg width="10" height="10" viewBox="0 0 24 24" style="margin-right:6px"><path d="M6 2l4 4-2 3c1 3 4 6 7 7l3-2 4 4-3 4C10 22 2 14 2 5z" fill="#fff"/></svg>555-014-2277</div>
  <nav class="nav">
    <span class="active">Home</span><span>About us</span><span>Services</span><span>Maintenance</span><span>Specials</span><span>Review</span><span>Faq's</span><span>Blog</span><span>Contact Us</span>
  </nav>

  <!-- Hero -->
  <div class="hero-photo" role="img" aria-label="Living room with wall-mounted air conditioner and a woman on a sofa holding a remote"></div>
  <svg class="abs" style="left:0;top:130px" width="1120" height="660" viewBox="0 0 1120 660">
    <path d="M0 530 C320 470 720 450 1120 330 L1120 660 L0 660Z" fill="#fff"/>
    <path d="M0 528 C320 468 720 448 1120 328" fill="none" stroke="#1a73e8" stroke-width="5"/>
    <path d="M1120 330 L1120 540 C1080 470 1020 420 940 405 C1000 385 1060 360 1120 330Z" fill="#1d1b5e"/>
  </svg>
  <div class="eyebrow">Servicing New Hampshire for 30 years</div>
  <h1 class="hero-title">HVAC Services and New install For<br>Residential &amp; Commercial</h1>
  <div class="btn btn-solid" style="left:98px;top:404px;width:180px;height:34px">Schedule an Appointment</div>
  <div class="badge" style="left:800px;top:170px"><b>30</b><span>YEARS OF<br>EXPERIENCE</span></div>

  <!-- Appointment form -->
  <aside class="form-panel">
    <h3>Schedule an Appointment</h3>
    <h4>24/7 FAST SERVICE</h4>
    <div class="field">Name</div>
    <div class="field">Email</div>
    <div class="field">Phone</div>
    <div class="field">Services <span>⌄</span></div>
    <div class="field tall">Description of requirement</div>
    <div class="submit">Submit</div>
    <div class="call-label">CALL FOR SERVICE</div>
    <div class="call-num">555–014–2277</div>
  </aside>

  <!-- About -->
  <h2 class="section-title" style="left:188px;top:700px">About Tidewell<br><b style="font-weight:600">Heating &amp; Air conditioning</b></h2>
  <p class="body-copy" style="left:188px;top:812px;width:380px">Lorem Ipsum is simply dummy text of the printing and typesetting industry. Lorem Ipsum has been the industry's standard dummy text ever since the 1500s, when an unknown printer took a galley of type and scrambled it to make a type specimen book. It has survived not only five centuries, but also the leap into electronic typesetting, remaining essentially unchanged. It was popularised in the 1960s with the release of Letraset sheets containing Lorem Ipsum passages, and more recently with desktop publishing software.</p>
  <div class="btn btn-outline" style="left:188px;top:956px;width:176px;height:34px">Schedule an Appointment</div>

  <!-- Why trust -->
  <h2 class="section-title center" style="left:0;top:1054px;width:1120px">See Why Customers trust<br>Tidewell HVAC</h2>
  <div class="rule" style="left:512px;top:1140px;width:96px"></div>
  <div class="trust-item" style="left:192px;top:1170px">
    <svg width="50" height="50" viewBox="0 0 50 50" fill="none" stroke="#1a73e8" stroke-width="2"><circle cx="25" cy="20" r="14"/><circle cx="25" cy="20" r="8" stroke="#1d1b5e"/><path d="M16 31l-4 15 8-4 5 6 M34 31l4 15-8-4-5 6"/></svg>
    We have over 30 years of heating and cooling experience</div>
  <div class="trust-item" style="left:386px;top:1170px">
    <svg width="50" height="50" viewBox="0 0 50 50" fill="none" stroke="#1a73e8" stroke-width="2"><rect x="10" y="4" width="26" height="40" rx="2" stroke="#1d1b5e"/><path d="M15 12h16M15 18h16M15 24h10M15 30h10"/><rect x="30" y="26" width="14" height="20"/></svg>
    We offer free HVAC free estimates</div>
  <div class="trust-item" style="left:578px;top:1170px">
    <svg width="50" height="50" viewBox="0 0 50 50" fill="none" stroke="#1a73e8" stroke-width="2"><rect x="5" y="6" width="40" height="18" rx="2" stroke="#1d1b5e"/><path d="M10 18h30M14 30v10M25 30v14M36 30v10"/></svg>
    We provide residential and commercial HVAC services</div>
  <div class="trust-item" style="left:772px;top:1170px">
    <svg width="50" height="50" viewBox="0 0 50 50" fill="none" stroke="#1a73e8" stroke-width="2"><path d="M8 42L30 20M30 20l6-10 6 2-4 8z" stroke="#1d1b5e"/><path d="M42 42L20 20M20 20c-6 2-12-4-10-10l5 5 5-5-5-5c6-2 12 4 10 10"/></svg>
    We offer HVAC maintenance plans</div>
  <div class="btn btn-outline" style="left:376px;top:1296px;width:178px;height:32px">Schedule an Appointment</div>
  <div class="btn btn-navy" style="left:574px;top:1296px;width:124px;height:32px">☎&nbsp; 555-014-2277</div>

  <!-- Service categories band -->
  <div class="services-bg" role="img" aria-label="Faded photo of a suburban house"></div>
  <svg class="abs" style="left:0;top:1350px" width="1120" height="200" viewBox="0 0 1120 200">
    <path d="M0 0 L1120 0 L1120 122 C760 150 420 140 50 20 L0 0Z" fill="#fff"/>
    <path d="M50 20 C420 140 760 150 1120 122" fill="none" stroke="#1a73e8" stroke-width="6"/>
  </svg>
  <div class="cat" style="left:278px;top:1400px;background:linear-gradient(160deg,#9aa3ae,#4d5664)" role="img" aria-label="Residential HVAC unit">Residential</div>
  <div class="cat" style="left:470px;top:1400px;background:linear-gradient(160deg,#8a8f97,#3e4450)" role="img" aria-label="Technicians at a commercial site">Commercial</div>
  <div class="cat" style="left:662px;top:1400px;background:linear-gradient(160deg,#6d7e96,#2f3b52)" role="img" aria-label="Technician installing equipment">Service and New<br>install</div>

  <h2 class="section-title center" style="left:0;top:1670px;width:1120px">Our Services</h2>
  <div class="card" style="left:186px;top:1746px"><svg width="40" height="32" viewBox="0 0 40 32" fill="none" stroke="#1d1b5e" stroke-width="2"><rect x="2" y="8" width="36" height="14" rx="2"/><path d="M8 16h24M14 4c4-3 8-3 12 0" stroke="#1a73e8"/></svg>Air Conditioning</div>
  <div class="card on" style="left:380px;top:1746px"><svg width="40" height="34" viewBox="0 0 40 34" fill="none" stroke="#fff" stroke-width="2"><rect x="22" y="2" width="6" height="22" rx="3"/><circle cx="25" cy="28" r="5"/><circle cx="10" cy="12" r="5"/><path d="M10 2v3M10 19v3M0 12h3M17 12h3"/></svg>Heating</div>
  <div class="card" style="left:574px;top:1746px"><svg width="40" height="32" viewBox="0 0 40 32" fill="none" stroke="#1d1b5e" stroke-width="2"><rect x="2" y="4" width="36" height="24" rx="2"/><circle cx="13" cy="16" r="7" stroke="#1a73e8"/><path d="M24 10h10M24 16h10M24 22h10"/></svg>Heat Pumps / Gas / Oil</div>
  <div class="card" style="left:768px;top:1746px"><svg width="40" height="32" viewBox="0 0 40 32" fill="none" stroke="#1d1b5e" stroke-width="2"><rect x="2" y="2" width="36" height="12" rx="2"/><path d="M10 20c2 3-2 5 0 8M17 20c2 3-2 5 0 8M24 20c2 3-2 5 0 8M31 20c2 3-2 5 0 8" stroke="#1a73e8"/></svg>Ductless Mini Splits</div>
  <div class="card" style="left:186px;top:1910px"><svg width="40" height="34" viewBox="0 0 40 34" fill="none" stroke="#1d1b5e" stroke-width="2"><circle cx="12" cy="10" r="7" stroke="#1a73e8"/><circle cx="28" cy="10" r="7" stroke="#1a73e8"/><path d="M6 20h28M12 20v12M20 20v12M28 20v12"/></svg>Controls</div>
  <div class="card" style="left:380px;top:1910px"><svg width="40" height="34" viewBox="0 0 40 34" fill="none" stroke="#1d1b5e" stroke-width="2"><rect x="6" y="2" width="28" height="10"/><rect x="12" y="14" width="16" height="18" stroke="#1a73e8"/><path d="M16 20h8M16 26h8"/></svg>VFD's</div>
  <div class="card" style="left:574px;top:1910px"><svg width="40" height="34" viewBox="0 0 40 34" fill="none" stroke="#1d1b5e" stroke-width="2"><rect x="4" y="1" width="32" height="32" rx="2"/><circle cx="20" cy="17" r="11" stroke="#1a73e8"/><path d="M20 6v22M9 17h22"/></svg>Pumps</div>
  <div class="card" style="left:768px;top:1910px"><svg width="40" height="34" viewBox="0 0 40 34" fill="none" stroke="#1d1b5e" stroke-width="2"><circle cx="20" cy="9" r="7" stroke="#1a73e8"/><path d="M20 16v6M4 22h32v8H4z"/></svg>Gas Fitting / Piping</div>
  <div class="btn btn-outline" style="left:376px;top:2080px;width:178px;height:32px">Schedule an Appointment</div>
  <div class="btn btn-navy" style="left:574px;top:2080px;width:124px;height:32px">☎&nbsp; 555-014-2277</div>

  <!-- Community -->
  <div class="community-photo" role="img" aria-label="Historic castle-style hotel above town buildings at sunset"></div>
  <div class="community-panel"></div>
  <h2 class="section-title" style="left:574px;top:2264px;color:#fff;font-size:22px">Proud to Serve Our Community<br>of Hampshire Areas</h2>
  <p class="body-copy light" style="left:574px;top:2366px;width:370px">Lorem Ipsum is simply dummy text of the printing and typesetting industry. Lorem Ipsum has been the industry's standard dummy text ever since the 1500s, when an unknown printer took a galley of type and scrambled it to make a type specimen book. It has survived not only five centuries, but also the leap into electronic typesetting, remaining essentially unchanged.</p>
  <div class="btn btn-ghost" style="left:574px;top:2498px;width:178px;height:34px">Schedule an Appointment</div>

  <!-- Reviews -->
  <div class="reviews-bg"></div>
  <svg class="abs" style="left:0;top:2560px" width="1120" height="240" viewBox="0 0 1120 240">
    <path d="M0 100 C300 98 560 80 760 60 C900 70 1020 120 1120 200 L1120 240 L0 240Z" fill="#f4f6f9"/>
    <path d="M700 66 C860 60 1000 110 1120 200" fill="none" stroke="#1a73e8" stroke-width="6"/>
  </svg>
  <div class="badge" style="left:752px;top:2550px"><b>30</b><span>YEARS OF<br>EXPERIENCE</span></div>

  <h2 class="section-title center" style="left:0;top:2706px;width:1120px">Happy Clients Say</h2>
  <div class="arrow" style="left:138px">‹</div>
  <div class="arrow" style="left:974px">›</div>
  <div class="review" style="left:186px"><div class="stars">★★★★★</div><p>"There are many variations of passages of Lorem Ipsum available, but the majority have suffered alteration in some form, by injected humour, or randomised..."</p></div>
  <div class="review" style="left:444px"><div class="stars">★★★★★</div><p>"There are many variations of passages of Lorem Ipsum available, but the majority have suffered alteration in some form, by injected humour, or randomised..."</p></div>
  <div class="review" style="left:702px"><div class="stars">★★★★★</div><p>"There are many variations of passages of Lorem Ipsum available, but the majority have suffered alteration in some form, by injected humour, or randomised..."</p></div>
  <div class="reviewer" style="left:214px"><span class="quote">“</span>Standard Chunk</div>
  <div class="reviewer" style="left:472px"><span class="quote">“</span>Finibus Bonorum</div>
  <div class="reviewer" style="left:730px"><span class="quote">“</span>J. Carver</div>
  <div class="btn btn-navy" style="left:300px;top:3014px;width:176px;height:32px;font-size:10px">Review Us on Findly</div>
  <div class="btn btn-outline" style="left:488px;top:3014px;width:146px;height:32px;font-size:10px">Review Us on TrustBureau</div>
  <div class="btn btn-outline" style="left:648px;top:3014px;width:178px;height:32px;font-size:10px">Review Us on Socialite</div>

  <!-- Partner seals -->
  <div class="seal" style="left:262px;top:3180px;width:60px;height:60px;border-radius:6px"></div>
  <div class="seal" style="left:390px;top:3180px;width:60px;height:60px;border-radius:50%"></div>
  <div class="seal" style="left:516px;top:3184px;width:60px;height:54px"></div>
  <div class="seal" style="left:644px;top:3178px;width:62px;height:62px;border-radius:50%"></div>
  <div class="seal" style="left:780px;top:3184px;width:74px;height:54px;border-radius:6px"></div>
  <div class="seal" style="left:358px;top:3290px;width:130px;height:34px;border-radius:4px"></div>
  <div class="seal" style="left:500px;top:3290px;width:80px;height:34px;border-radius:4px"></div>
  <div class="seal" style="left:608px;top:3282px;width:100px;height:42px;border-radius:4px"></div>

  <!-- Careers -->
  <div class="careers" role="img" aria-label="Dark blue tinted photo of an HVAC technician at work"></div>
  <svg class="abs" style="left:0;top:3330px" width="1120" height="160" viewBox="0 0 1120 160">
    <path d="M0 0 L1120 0 L1120 110 C760 120 360 90 0 10Z" fill="#fff"/>
    <path d="M30 20 C360 100 760 130 1120 112" fill="none" stroke="#1a73e8" stroke-width="6"/>
  </svg>
  <h2 class="careers-title">Join Our Team<br>Careers at Tidewell HVAC</h2>
  <p class="careers-copy">We're always interested in speaking with talented, driven individuals to join our team.<br>If you have a strong work ethic and are committed to excellence?</p>
  <div class="btn btn-ghost" style="left:500px;top:3670px;width:120px;height:32px;color:var(--blue-soft)">Join Our Team</div>

  <!-- Footer -->
  <div class="brand" style="left:98px;top:3910px;font-size:24px"><span class="brand-dot" style="width:36px;height:36px"></span>Tidewell HVAC</div>

  <div class="foot-h" style="left:380px;top:3852px">Contact Us</div>
  <ul class="foot-list" style="left:380px;top:3880px;width:200px">
    <li class="contact-row"><span style="color:var(--blue)">☎</span>555 014-3080</li>
    <li class="contact-row" style="margin-top:4px"><span style="color:var(--blue)">✉</span>hello@tidewellhvac.example</li>
    <li class="contact-row" style="margin-top:4px"><svg width="9" height="12" viewBox="0 0 12 16" style="margin-top:3px"><path d="M6 0C2.7 0 0 2.7 0 6c0 4.5 6 10 6 10s6-5.5 6-10c0-3.3-2.7-6-6-6z" fill="#1a73e8"/></svg><span><span style="color:var(--blue)">Tidewell HVAC</span><br>34 Millbrook Lane,<br>Eastfield, NH</span></li>
  </ul>

  <div class="foot-h" style="left:608px;top:3852px">Quick Links</div>
  <ul class="foot-list" style="left:608px;top:3880px">
    <li>Home</li><li>About us</li><li>Services</li><li>Maintenance</li><li>Specials</li><li>Contact Us</li>
  </ul>
  <ul class="foot-list" style="left:720px;top:3880px">
    <li>Review</li><li>Faq's</li><li>Blog</li><li>Careers</li>
  </ul>

  <div class="foot-h" style="left:836px;top:3852px">Working Hours</div>
  <ul class="foot-list" style="left:836px;top:3880px;width:200px">
    <li style="display:flex;justify-content:space-between"><span>Monday to Friday:</span><span style="width:86px">11am – 6pm</span></li>
    <li style="display:flex;justify-content:space-between"><span>Saturday:</span><span style="width:86px">11am – 5pm</span></li>
    <li style="display:flex;justify-content:space-between"><span>Sunday:</span><span style="width:86px">By appointment</span></li>
  </ul>
  <div class="foot-h" style="left:836px;top:3944px">Follow Us</div>
  <span class="social" style="left:836px"></span>
  <span class="social" style="left:864px;background:var(--navy);border-color:var(--navy)"></span>
  <span class="social" style="left:892px"></span>

  <div class="legal" style="left:98px">© 2024 <b>Tidewell HVAC</b>. All Right Reserved</div>
  <div class="legal" style="left:380px">Terms and Conditions &nbsp;|&nbsp; Privacy Policy</div>
  <svg class="abs" style="left:1054px;top:4070px" width="14" height="16" viewBox="0 0 14 16"><path d="M7 0L14 16 7 11 0 16Z" fill="#1a73e8"/></svg>

</div>
</body>
</html>
```